Website for Boutique Property Consultancy in UK

We are looking to designing a website for our Property Consultancy Services that follows a minimalistic clean style that is also bold and intriguing.
The website will be based on one landing page and a link to LinkedIn Page and email link.

Dominant features will be the company logo or icon and colours.

Brand colours provided for guidance.

Looking to achieve a minimalistic clean style that is also bold and intriguing.

"Updated"
Page 1 - Landing Page with the Hyperlinks to Pick a Service, Training Portal and Amber Quill Portal. example landing page https://plumweave.co.uk/

Page 2 - Shows all the Services and Sectors

Target Market(s)

Occupier Clients, Tech Companies, Property Developers, Infrastructure Clients and Major Consultants

Industry/Entity Type

Construction

Coding

Coded - Design and coding required

Number of Pages Required

2 page

Font styles to use
Other font styles liked:
• Century Gothic or Futuris (Headings)

Colors
0054AA
0677BA
7BADD7
CADEEF
E8F1F8
00AB8E
00BBA5
67D7C9
C6EFE9
E9F9F6

Requirements
Must have
• Company Logo, link to enquiry and LinkedIn

```html
<!DOCTYPE html>
<html lang="en">
<head>
<meta charset="utf-8">
<title>Verra Lume</title>
<link rel="stylesheet" href="https://fonts.googleapis.com/css2?family=Raleway:wght@300;400;500&family=Varela+Round&display=swap">
<style>
  :root {
    --night-deep: #141d33;
    --night-mid: #26365e;
    --night-sky: #3a4f80;
    --river-glow: #4a5a6e;
    --ink-white: #ffffff;
    --grid-line: rgba(255, 255, 255, 0.35);
    --brand-teal: #00bba5;
  }
  * { margin: 0; padding: 0; box-sizing: border-box; }
  html, body { width: 1200px; height: 625px; overflow: hidden; }
  body { font-family: "Raleway", sans-serif; color: var(--ink-white); background: var(--night-deep); }
  .landing { position: relative; width: 1200px; height: 625px; overflow: hidden; }
  .hero-photo {
    position: absolute; inset: 0;
    background:
      radial-gradient(ellipse at 55% 45%, rgba(120, 130, 110, 0.35), transparent 55%),
      linear-gradient(180deg, var(--night-sky) 0%, var(--night-mid) 35%, var(--river-glow) 65%, var(--night-deep) 100%);
  }
  .hero-shade { position: absolute; inset: 0; background: rgba(20, 30, 70, 0.35); }
  .grid-line { position: absolute; top: 0; bottom: 0; width: 1px; background: var(--grid-line); }
  .brand {
    position: absolute; top: 22px; left: 0; right: 0; text-align: center;
    font-family: "Raleway", sans-serif; font-weight: 400; font-size: 44px; letter-spacing: 1px;
    color: var(--ink-white); text-decoration: none;
  }
  .menu-toggle { position: absolute; left: 1066px; top: 26px; width: 34px; height: 25px; }
  .menu-toggle span { position: absolute; right: 0; height: 3px; background: var(--ink-white); border-radius: 2px; }
  .menu-toggle span:nth-child(1) { top: 0; width: 28px; }
  .menu-toggle span:nth-child(2) { top: 11px; width: 34px; }
  .menu-toggle span:nth-child(3) { top: 22px; width: 22px; }
  .tagline {
    position: absolute; top: 272px; left: 0; right: 0; text-align: center;
    font-weight: 300; font-size: 32px; letter-spacing: -0.2px;
  }
  .service-links {
    position: absolute; top: 324px; left: 0; right: 0; text-align: center;
    font-family: "Varela Round", sans-serif; font-size: 38px; letter-spacing: -0.3px;
  }
  .service-links a { color: var(--ink-white); text-decoration: none; margin: 0 3px; }
  .copyright { position: absolute; left: 150px; top: 589px; font-size: 14px; font-weight: 400; }
  .contact { position: absolute; right: 102px; top: 583px; display: flex; align-items: center; gap: 8px; }
  .contact-label { font-size: 14px; margin-right: 4px; }
  .contact-icon {
    width: 30px; height: 30px; border-radius: 50%; background: var(--brand-teal);
    display: flex; align-items: center; justify-content: center;
  }
</style>
</head>
<body>
  <main class="landing">
    <div class="hero-photo" role="img" aria-label="Night view of a city river with a stone arch bridge between office and apartment buildings"></div>
    <div class="hero-shade"></div>

    <div class="grid-line" style="left:150px"></div>
    <div class="grid-line" style="left:450px"></div>
    <div class="grid-line" style="left:750px"></div>
    <div class="grid-line" style="left:1050px"></div>

    <a class="brand" href="#">verra lume</a>

    <div class="menu-toggle" aria-label="Menu"><span></span><span></span><span></span></div>

    <p class="tagline">Delivering Value and Redefining Boundaries</p>
    <nav class="service-links">
      <a href="#">#pick-a-service</a>
      <a href="#">#training-portal</a>
      <a href="#">#amber-quill</a>
    </nav>

    <p class="copyright">©Copyright ©2023 Verra Lume. All Rights Reserved.</p>

    <div class="contact">
      <span class="contact-label">By Referral Only</span>
      <a class="contact-icon" href="#" aria-label="Email">
        <svg width="16" height="12" viewBox="0 0 16 12" fill="none" stroke="#fff" stroke-width="1.5">
          <rect x="0.75" y="0.75" width="14.5" height="10.5"/>
          <path d="M1 1l7 5.5L15 1M1 11l5-4.5M15 11l-5-4.5"/>
        </svg>
      </a>
      <a class="contact-icon" href="#" aria-label="Professional profile"></a>
    </div>
  </main>
</body>
</html>
```